Vodka Bottle Label - Lune Vodka

I need a bottle label for a vodka I'd like to make called Lune Vodka.
I would like a label that looks elegant and fresh. I would like some mountains and colours to be red and white. Open to other colours being added but not too colourful. "Lune" means fresh, dawn in polish, i would like if mountains or something extra was added to the label too. I would like the Lune Vodka name not to be too small.
The vodka is made in australia and is 37%.

I would love to have a little bit of gold colour in the label!

I will provide the back label words when completing my decision.

i'd like to make it more simple and less european looking. More australian.

I saw a bottle like this and i did like the concept.

https://www.oakbarrelcellars.com.au/spirits/grey-vodka-range?srsltid=XqTz81mwkPLd04-hr-q7w93nfbzkgd_mR2yTpaMWxJeQ6vcbTnZsLpo

Target Market(s)

Vodka Drinkers

Industry/Entity Type

Alcohol

Colors
EB3D1F
EC4F4E
F09395
F8D3D4
FCEDEE

Requirements
Must have
• red and white colours incorporated, mountains or freshness on it.
Nice to have
• Fresh and clean look. Classy

```html
<!DOCTYPE html>
<html lang="en">
<head>
<meta charset="utf-8">
<title>Lune Vodka – Bottle Label</title>
<link rel="stylesheet" href="https://fonts.googleapis.com/css2?family=Montserrat:wght@700;800&family=Oswald:wght@400&display=swap">
<style>
  :root {
    --canvas: #ffffff;
    --label-black: #000000;
    --label-red: #e2401f;
    --emblem-fill: #2f8fcf;
  }
  * { margin: 0; padding: 0; box-sizing: border-box; }
  html, body {
    width: 849px;
    height: 1200px;
    overflow: hidden;
    background: var(--canvas);
  }
  .canvas {
    position: relative;
    width: 849px;
    height: 1200px;
  }
  .label {
    position: absolute;
    left: 229px;
    top: 50px;
    width: 391px;
    height: 1100px;
    background: var(--label-black);
  }
  .label-frame {
    position: absolute;
    left: 14px;
    top: 17px;
    right: 14px;
    bottom: 17px;
    border: 2.5px solid var(--label-red);
  }
  .brand {
    position: absolute;
    top: 238px;
    left: 0;
    width: 100%;
    text-align: center;
    color: var(--label-red);
    font-family: "Montserrat", "Helvetica Neue", Arial, sans-serif;
  }
  .brand-name {
    display: block;
    font-size: 67px;
    font-weight: 800;
    line-height: 1;
    letter-spacing: 0.02em;
    padding-left: 0.02em;
  }
  .brand-type {
    display: block;
    margin-top: 12px;
    font-size: 25px;
    font-weight: 800;
    line-height: 1;
    letter-spacing: 0.95em;
    padding-left: 0.95em;
  }
  .emblem {
    position: absolute;
    left: 82px;
    top: 376px;
    width: 228px;
    height: 234px;
  }
  .details {
    position: absolute;
    left: 51px;
    right: 40px;
    top: 1035px;
    display: flex;
    justify-content: space-between;
    color: var(--label-red);
    font-family: "Oswald", "Arial Narrow", sans-serif;
    font-size: 27px;
    font-weight: 400;
    line-height: 1;
  }
  .details .abv { margin-right: 15px; }
</style>
</head>
<body>
  <main class="canvas">
    <section class="label">
      <div class="label-frame"></div>

      <h1 class="brand">
        <span class="brand-name">LUNE</span>
        <span class="brand-type">VODKA</span>
      </h1>

      <svg class="emblem" viewBox="0 0 228 234" role="img" aria-label="Round emblem illustration: a rising sun over rolling fields">
        <circle cx="114" cy="117" r="111" fill="var(--label-black)" stroke="var(--label-red)" stroke-width="2.5"/>
        <circle cx="114" cy="117" r="104" fill="var(--emblem-fill)"/>
      </svg>

      <p class="details">
        <span class="volume">250mL</span>
        <span class="abv">37% ALCOHOL</span>
      </p>
    </section>
  </main>
</body>
</html>
```